Business Card Design Project

Kestrel Amber Ridge Farms, LLC is a small farm south of Bandon Oregon. The farm produces blueberries, cranberries, mushrooms and possible other crops in the future.
We plan on installing yurts on the property for rent and for a farm experience,

A clody/misty covered black moon should be the design. This could be the entire front of the card. (There is another pixel harbor project for this design). The back could be for the names, phone, address, etc.

Another option would be 3/4 of the card be the logo, then put the name, title, address, etc. vertically on the card right side front.

Target Market(s)

Customers of the farm, possible visitors using the yurts,

Industry/Entity Type

Farm

Other font styles liked:
• Hobo std

Colors

Designer to choose colors to be used in the design.

Requirements
Must have
• Consistent font usage

```html
<!DOCTYPE html>
<html lang="en">
<head>
<meta charset="utf-8">
<title>Kestrel Amber Ridge Farms – Business Card</title>
<link rel="stylesheet" href="https://fonts.googleapis.com/css2?family=Kalam:wght@400;700&display=swap">
<style>
  :root {
    --backdrop: #b3c1c1;
    --card-front: #f4f3ef;
    --ink: #1a1a1a;
    --frame: #0d0d0d;
    --wash-light: #d9e0df;
    --wash-mid: #b9c6c5;
    --back-center: #3a3a3a;
    --back-edge: #0b0b0b;
    --back-text: #e8e8e8;
    --back-soft: #c9cfcf;
  }
  * { box-sizing: border-box; margin: 0; padding: 0; }
  html, body { width: 1200px; height: 900px; overflow: hidden; }
  body {
    background: var(--backdrop);
    font-family: "Kalam", cursive;
    position: relative;
  }
  .card {
    position: absolute;
    top: 302px;
    width: 520px;
    height: 297px;
    border-radius: 22px;
    box-shadow: 0 10px 22px rgba(0,0,0,0.18);
    overflow: hidden;
  }
  .card-front { left: 50px; background: var(--card-front); }
  .card-front .frame {
    position: absolute;
    inset: 12px;
    border: 5px solid var(--frame);
    border-radius: 16px;
  }
  .farm-name {
    position: absolute;
    top: 50px;
    left: 0; right: 0;
    text-align: center;
    font-size: 25px;
    font-weight: 400;
    color: var(--ink);
    letter-spacing: 0.5px;
    white-space: nowrap;
  }
  .moon-art {
    position: absolute;
    top: 92px;
    left: 150px;
    width: 220px;
    height: 118px;
    display: block;
  }
  .location {
    position: absolute;
    top: 212px;
    left: 0; right: 0;
    text-align: center;
    font-size: 24px;
    color: var(--ink);
    white-space: nowrap;
  }
  .card-back {
    left: 630px;
    background: radial-gradient(ellipse at 50% 45%, var(--back-center) 0%, #1c1c1c 55%, var(--back-edge) 100%);
    color: var(--back-text);
    text-align: center;
  }
  .contact {
    position: absolute;
    top: 64px;
    left: 0; right: 0;
  }
  .person-name { font-size: 26px; color: var(--back-soft); line-height: 1.1; }
  .person-title { font-size: 15px; font-style: italic; color: var(--back-text); }
  .address { margin-top: 26px; font-size: 17px; line-height: 1.3; }
  .phone { margin-top: 4px; font-size: 26px; font-weight: 700; letter-spacing: 1px; }
  .web { font-size: 16px; white-space: nowrap; }
</style>
</head>
<body>
  <section class="card card-front">
    <div class="frame"></div>
    <h1 class="farm-name">Kestrel Amber Ridge Farms</h1>
    <svg class="moon-art" viewBox="0 0 220 118" role="img" aria-label="Watercolour illustration of a black moon wrapped in white mist">
      <defs>
        <linearGradient id="wash" x1="0" y1="0" x2="1" y2="1">
          <stop offset="0" stop-color="#d9e0df"/>
          <stop offset="1" stop-color="#b9c6c5"/>
        </linearGradient>
      </defs>
      <rect x="0" y="0" width="220" height="118" fill="url(#wash)"/>
    </svg>
    <p class="location">Coral Bend, Oregon</p>
  </section>

  <section class="card card-back">
    <div class="contact">
      <p class="person-name">Daniel Forsyth</p>
      <p class="person-title">President</p>
      <p class="address">4127 Heron Crest Lane<br>Coral Bend, Oregon 97432</p>
      <p class="phone">541-555-0142</p>
      <p class="web">www.kestrelamberridgefarms.com</p>
    </div>
  </section>
</body>
</html>
```